Bright Harbor Christmas Gifts Donations Catalogue

We need a catalog that will help us solicit donations for Christmas gifts for people in developing countries. We are looking at a 5.5 X 8.5 booklet format with this format:

1- cover
2- whole page for child sponsorship
3- Water (filter and tank)
4- Animals (cow, pig)
5- Farming (fertilizer, seeds)
6- Children (school supplies, nutritious meals)
7- Health (medicine, mosquito nets)
8- Back

1. The front cover should say: "Bright Harbor Christmas Gift Catalogue.... This Christmas, give the gift of hope."

2:child sponsorship- $30/mo.
(For $30 per month, you can change a child's future.

Your sponsorship provides school tuition, school uniforms, school supplies, and a daily meal for your child.

Your sponsorship provides:

Nutrition
Clean Water
Healthcare
Education

3. Keller clear two water filter- $65
(Provide a lifetime supply of clean drinking water and sanitation training for at least one family).
Water tank- $3500
(Provides a community with safe drinking water)
Contribute toward a water tank- $25, $50, $100, other
4. Milking Cow- $500
(A good, mature milking cow provides $8 per day in income for a family and milk for the community)
A pig- $50
(Provide a family with a source of income. Pigs are easy to maintain, produce manure, and families can sell the offspring.)
5. Fertilizer- $40
(Fertilizer for the school farms will increase their productivity, thus providing more nourishment for the students)
Seeds- $10
(Provide a family seeds so that they can provide for themselves
6. Meals for school children- $10.
(You can provide much needed nourishment for hungry children)
School supplies and uniforms- $40
(Education enables children to reach their full potential and escape from the cycle of poverty.)
7. Medicine- $25
($25 provides medicine for 10 people. $500 provides the medicine for a full day of outreach clinics.)
Mosquito Nets- $20
Help protect a family from life-threatening diseases like malaria.
8. The most meaningful gifts you can give or receive this Christmas.

Bright Harbor is a Christian organization that brings hope and restoration to the poor and vulnerable in the developing world through both supernatural and practical expressions of the Kingdom of God.

To give a gift of hope, donate at www.brightharbor.org

The design should be fairly consistent with the feel of our website (www.brightharbor.org). The design should work for an online catalog as well as for a printed format.

We are basically looking for something like Open Meadow's Christmas gift catalogs. An example: https://www.findexo.example/search?q=holiday+gift+booklets

I have just updated my brief- added photos and examples.  I would like a picture to be the background on the front cover.  

Thank you!

I realized that it's going to be too tight trying to fit everything onto two pages, so I'm going to add a page to the booklet (so there will be 8 half pages now).  Here's the new format:

1- cover
4- Animals (cow, pig)
8- Back

I added some more of our pictures.  They may be helpful?

Target Market(s)

Mostly Christians. Families and individuals who want to make a difference during the Christmas season.

Industry/Entity Type

Training

Requirements
Must have
• Pictures of each item (real picures- no clip-art) , a place for a short description of each item, and the price
Nice to have
• A nice cover page (with a captivating picture)
Some of our pictures from our facebook page: https://www.socialhub.example/brightharborministries/photos_stream
Should not have
• Clip-art

```html
<!DOCTYPE html>
<html lang="en">
<head>
<meta charset="utf-8">
<title>Bright Harbor Christmas Gift Catalogue – Animals &amp; Farming</title>
<link rel="stylesheet" href="https://fonts.googleapis.com/css2?family=Barlow+Semi+Condensed:wght@700&family=Barlow:wght@700&family=Crimson+Text:ital@1&family=Shadows+Into+Light+Two&display=swap">
<style>
  :root {
    --sky: #00adef;
    --navy: #1c5f9e;
    --ink: #231f20;
    --paper: #ffffff;
    --holly: #d3202e;
    --rule: #6d6e70;
  }
  * { margin: 0; padding: 0; box-sizing: border-box; }
  html, body { width: 1200px; height: 927px; overflow: hidden; background: var(--paper); }
  .spread { position: relative; width: 1200px; height: 927px; background: var(--paper); }
  .band { position: absolute; left: 0; top: 82px; width: 1200px; height: 463px; background: var(--sky); }
  .fold { position: absolute; left: 599px; top: 0; width: 2px; height: 927px; background: var(--rule); }
  .tagline {
    position: absolute; top: 26px;
    font-family: "Shadows Into Light Two", cursive;
    font-size: 27px; color: var(--holly); white-space: nowrap;
  }
  .tagline--lead { left: 30px; }
  .tagline--close { right: 32px; }

  .gift { position: absolute; width: 540px; height: 260px; }
  .gift__title {
    position: absolute; left: 0; top: 0;
    font-family: "Barlow Semi Condensed", sans-serif; font-weight: 700;
    font-size: 46px; line-height: 1; color: var(--navy); letter-spacing: 0.5px;
  }
  .gift__price {
    position: absolute; left: 0; top: 52px;
    font-family: "Barlow", sans-serif; font-weight: 700;
    font-size: 28px; line-height: 1;
  }
  .gift__text {
    position: absolute; left: 0; top: 112px; width: 250px;
    font-family: "Crimson Text", serif; font-style: italic;
    font-size: 22px; line-height: 27px;
  }
  .gift--featured .gift__price, .gift--featured .gift__text { color: var(--paper); }
  .gift--plain .gift__price, .gift--plain .gift__text { color: var(--ink); }

  .gift__photo {
    position: absolute; width: 258px; height: 207px;
    border-radius: 13px; border: 6px solid;
  }
  .gift--featured .gift__photo { border-color: var(--paper); }
  .gift--plain .gift__photo { border-color: var(--navy); }

  .photo--cow { background: linear-gradient(160deg, #b9d6ef 0%, #8fb7dc 45%, #3d3a3a 70%, #e8e4df 100%); }
  .photo--farm { background: linear-gradient(180deg, #d8e6e4 0%, #6f9b4c 35%, #5a3d2a 65%, #8a5a3d 100%); }
  .photo--pig { background: linear-gradient(180deg, #bcdcf0 0%, #e9c6b3 40%, #f0cdb9 62%, #5f8f36 100%); }
  .photo--seeds { background: radial-gradient(circle at 50% 50%, #e4cfa6 0%, #c9a878 55%, #a8845a 100%); }
</style>
</head>
<body>
<main class="spread">
  <div class="band"></div>
  <div class="fold"></div>

  <p class="tagline tagline--lead">This Christmas ...</p>
  <p class="tagline tagline--close">... give the gift of hope.</p>

  <section class="gift gift--featured" style="left:53px; top:234px;">
    <h2 class="gift__title">MILKING COW</h2>
    <p class="gift__price">$500</p>
    <p class="gift__text">A good, mature milking cow provides $8 per day in income for a family and milk for the community.</p>
  </section>
  <div class="gift--featured"><div class="gift__photo photo--cow" role="img" aria-label="Close-up of a black and white dairy cow against a blue sky" style="left:308px; top:298px;"></div></div>

  <section class="gift gift--featured" style="left:638px; top:234px;">
    <h2 class="gift__title">FERTILISER</h2>
    <p class="gift__price">$40</p>
    <p class="gift__text">Fertilizer for the school farms will increase their productivity, thus providing more nourishment for the students.</p>
  </section>
  <div class="gift--featured"><div class="gift__photo photo--farm" role="img" aria-label="Students working the soil on a school farm" style="left:908px; top:298px;"></div></div>

  <section class="gift gift--plain" style="left:51px; top:614px;">
    <h2 class="gift__title">A PIG</h2>
    <p class="gift__price" style="top:55px;">$50</p>
    <p class="gift__text">Provide a family with a source of income. Pigs are easy to maintain, produce manure, and families can sell the offspring.</p>
  </section>
  <div class="gift--plain"><div class="gift__photo photo--pig" role="img" aria-label="A pink pig grazing on green grass" style="left:308px; top:660px;"></div></div>

  <section class="gift gift--plain" style="left:636px; top:614px;">
    <h2 class="gift__title">SEEDS</h2>
    <p class="gift__price" style="top:55px;">$10</p>
    <p class="gift__text">Provide a family seeds so that they can provide for themselves.</p>
  </section>
  <div class="gift--plain"><div class="gift__photo photo--seeds" role="img" aria-label="A close-up pile of grain seeds" style="left:908px; top:660px;"></div></div>
</main>
</body>
</html>
```